PLV Roofing- Bold Web Design Project

We need a website design for a company that constructs and repairs commercial and residential roofing. They need a website design that looks clean, cutting edge, and can keep up with their competitors websites (Norvane Summit, Fulford Roofing Company, TWL Construction). They want to look experienced and "big" enough to handle large commercial projects. They also are striving for a professional and educational feel, and want to really articulate that they work with both residential/HOA and commercial clientele. They want a high conversion rate to their social media platforms and to another area of the site where they can fill out a form, so those areas should be emphasized.

Target Market(s)

Men and Women mainly between 25 and 65, typically in the higher income bracket (200,000+).

Industry/Entity Type

Residential

Requirements
Must have
• Landing page must have two separate but equally prominent buttons, directing the customers to a specific area of the site based on their need: commercial or residential. Clicking ether of these links will lead them to a welcome page for residential customers, or a welcome page for commercial clients.
-So must have 2 pages, a landing page and a welcome page that can be adapted for use as the commercial page and the residential page.
- A photo slider on the landing page
Nice to have
• -Color scheme should generally follow along with the colors used in the logo
-Professional, bold and modern.
Should not have
• -Avoid the "mom and pop" look
-Avoid the color red in the color scheme

```html
<!DOCTYPE html>
<html lang="en">
<head>
<meta charset="utf-8">
<title>PLV Network — Construction &amp; Disaster Management</title>
<link href="https://fonts.googleapis.com/css2?family=Roboto+Condensed:wght@400;700&family=Tinos:wght@400;700&display=swap" rel="stylesheet">
<style>
:root{
  --ink:#222;
  --heading:#444;
  --body-text:#777;
  --muted:#888;
  --rule:#d8d8d8;
  --band:#e1e1e1;
  --paper:#fcfcfa;
  --white:#fff;
  --lime:#8cc63f;
  --lime-light:#dbf2b3;
  --lime-deep:#a2d257;
  --orange:#f39a1e;
  --dark:#2a2a2a;
  --dark-2:#4a4a4a;
}
*{box-sizing:border-box;margin:0;padding:0}
html,body{width:1020px;height:1200px;overflow:hidden}
body{position:relative;background:var(--paper);font-family:"Roboto Condensed",Arial,sans-serif;color:var(--ink)}
.abs{position:absolute}

/* header */
.site-header{left:0;top:0;width:1020px;height:86px;background:var(--white);box-shadow:0 2px 4px rgba(0,0,0,.15);z-index:3}
.brand{left:65px;top:18px;display:flex;align-items:center;gap:8px}
.brand-mark{width:16px;height:16px;background:var(--lime)}
.brand-name{font-weight:700;font-size:26px;color:var(--ink);line-height:1}
.brand-tag{left:65px;top:50px;font-size:8px;letter-spacing:.3px;color:var(--ink)}
.main-nav{left:453px;top:0;height:86px;display:flex}
.nav-item{position:relative;height:86px;display:flex;flex-direction:column;align-items:center;padding-top:16px;font-size:12px;color:#555;border-left:1px solid #eee}
.nav-item svg{width:28px;height:28px;margin-bottom:9px}
.nav-item.is-active{background:linear-gradient(#f0f0f0,var(--lime-light) 70%,#c7e88f);color:#555}
.nav-item.is-active::after{content:"";position:absolute;bottom:-8px;left:50%;margin-left:-12px;width:24px;height:12px;border-radius:0 0 12px 12px;background:#c7e88f}

/* hero */
.hero-band{left:0;top:86px;width:1020px;height:369px;background:var(--band)}
.slider{left:193px;top:94px;width:638px;height:279px;border:2px solid #c9c9c9;background:linear-gradient(180deg,#c7a178 0%,#e7d7c0 40%,#d8c9b6 70%,#9e8d7d 100%)}
.slider-dots{left:440px;top:351px;width:120px;height:28px;border-radius:14px;background:var(--white);box-shadow:0 2px 3px rgba(0,0,0,.25);display:flex;align-items:center;justify-content:center;gap:6px}
.slider-dots span{width:17px;height:17px;border-radius:50%;background:radial-gradient(circle at 40% 35%,#fff,#cfcfcf)}
.slider-dots span.is-current{background:#111}

.entry-card{top:389px;width:251px;height:131px;background:linear-gradient(var(--lime-light),var(--lime-deep));border:1px solid #b7dd7d;text-align:center;font-size:23px;line-height:34px;padding-top:18px;color:#1d1d1d}
.entry-card.commercial{left:258px}
.entry-card.residential{left:517px}
.entry-card .cta{position:absolute;top:99px;width:78px;height:24px;border-radius:12px;background:linear-gradient(#fff,#e4e4e4);border:1px solid #bbb;font-size:13px;line-height:22px;color:#555}
.entry-card.commercial .cta{left:76px}
.entry-card.residential .cta{left:132px}

/* content */
.col-title{top:557px;font-size:21px;color:var(--heading);font-weight:400}
.thumb{top:599px;width:159px;height:101px;border:2px solid #eee;background:var(--white);padding:4px}
.thumb div{width:100%;height:100%}
.thumb-apple{background:radial-gradient(circle at 50% 55%,#8fd13d 0,#6cb02a 30%,#fff 33%)}
.thumb-team{background:linear-gradient(90deg,#fff 12%,#2b2b2b 12%,#3a3a3a 50%,#bfc7d4 70%,#2b2b2b 88%,#fff 88%)}
.thumb-globe{background:radial-gradient(circle at 48% 40%,#6fa8dc 0,#3a78c2 22%,#fff 25%)}
.col-text{width:210px;font-size:14px;line-height:18.6px;color:var(--body-text);word-break:break-all}
.col-text p+p{margin-top:18px}
.bullets{list-style:none;font-size:14px;line-height:18.6px;color:var(--body-text)}
.bullets li{position:relative;padding-left:14px;margin-bottom:18px}
.bullets li::before{content:"";position:absolute;left:0;top:8px;width:3px;height:3px;background:#888}

/* footer */
.footer-band{left:0;top:965px;width:1020px;height:160px;background:var(--band)}
.foot-title{top:991px;font-size:19px;font-weight:700;color:#444}
.foot-links{list-style:none;font-family:"Tinos",serif;font-size:11px;line-height:20px;color:#555}
.foot-links li::before{content:"";display:inline-block;width:3px;height:3px;background:#777;margin:0 6px 2px 0}
.social-row{display:flex;gap:12px;font-family:"Tinos",serif;font-size:10.5px;line-height:11px;color:#444}
.social-icon{width:20px;height:20px;flex:none}
.newsletter{left:706px;top:992px;width:187px;height:121px;border:1px solid #999;background:linear-gradient(var(--dark),var(--dark-2));color:var(--white)}
.newsletter h3{font-family:"Tinos",serif;font-weight:700;font-size:17px;text-align:center;margin-top:13px;padding-bottom:4px;border-bottom:2px solid #666;margin-left:14px;margin-right:14px}
.email-field{position:absolute;left:12px;top:52px;width:162px;height:22px;border-radius:4px;background:var(--white);color:#222;font-family:"Tinos",serif;font-size:14px;line-height:22px;padding-left:10px}
.email-go{position:absolute;right:0;top:0;width:24px;height:22px;border-radius:0 4px 4px 0;background:var(--orange);color:#fff;font-size:14px;line-height:20px;text-align:center;font-weight:700}
.subscribe{position:absolute;left:16px;top:81px;font-family:"Tinos",serif;font-size:12px;color:#888;text-decoration:underline}

.bottom-bar{left:0;top:1125px;width:1020px;height:75px;background:var(--paper)}
.bottom-links{left:92px;top:1146px;font-size:14.5px;color:#222;word-spacing:2px}
.bottom-links span{margin:0 14px;color:#555}
.rights{left:713px;top:1146px;font-size:14.5px;color:#222}
.rights span{margin:0 14px;color:#555}
</style>
</head>
<body>

<header class="abs site-header">
  <div class="abs brand"><span class="brand-mark"></span><span class="brand-name">PLV Network</span></div>
  <div class="abs brand-tag">CONSTRUCTION &amp; DISASTER MANAGEMENT</div>
  <nav class="abs main-nav">
    <div class="nav-item is-active" style="width:78px">
      <svg viewBox="0 0 28 28"><path d="M4 14 14 5l10 9" fill="none" stroke="#444" stroke-width="2.5"/><rect x="7" y="13" width="14" height="11" fill="#555"/><rect x="12" y="17" width="4" height="7" fill="#eee"/></svg>Home</div>
    <div class="nav-item" style="width:72px">
      <svg viewBox="0 0 28 28"><rect x="6" y="3" width="16" height="22" fill="#bbb" stroke="#777"/><rect x="9" y="3" width="13" height="22" fill="#ddd"/></svg>About PLV</div>
    <div class="nav-item" style="width:110px">
      <svg viewBox="0 0 28 28"><circle cx="14" cy="14" r="12" fill="#666"/><rect x="12.5" y="12" width="3" height="9" fill="#fff"/><circle cx="14" cy="8" r="1.8" fill="#fff"/></svg>Consulting Services</div>
    <div class="nav-item" style="width:69px">
      <svg viewBox="0 0 28 28"><circle cx="14" cy="8" r="5.5" fill="#333"/><path d="M4 27c0-9 4-13 10-13s10 4 10 13z" fill="#444"/></svg>Clients</div>
    <div class="nav-item" style="width:104px">
      <svg viewBox="0 0 28 28"><rect x="4" y="4" width="20" height="20" fill="#777"/><path d="M7 7h14v9l-7 5-7-5z" fill="#eee"/></svg>News &amp; Events</div>
    <div class="nav-item" style="width:112px">
      <svg viewBox="0 0 28 28"><circle cx="14" cy="14" r="12" fill="#555"/><path d="M14 2a12 12 0 0 1 12 12H14zM2 14a12 12 0 0 0 12 12V14z" fill="#aaa"/></svg>Contact PLV</div>
  </nav>
</header>

<div class="abs hero-band"></div>
<div class="abs slider" role="img" aria-label="Slider photo of a bright office lobby with wood ceiling and polished floor"></div>
<div class="abs slider-dots"><span class="is-current"></span><span></span><span></span><span></span></div>

<a class="abs entry-card commercial">Welcome<br>Commerical Page<span class="cta">Click Here</span></a>
<a class="abs entry-card residential">Welcome<br>Residential Page<span class="cta">Click Here</span></a>

<h2 class="abs col-title" style="left:147px">Who We Are</h2>
<h2 class="abs col-title" style="left:399px">Our Profile</h2>
<h2 class="abs col-title" style="left:707px">Latest News</h2>

<div class="abs thumb" style="left:147px"><div class="thumb-apple" role="img" aria-label="Photo of a green apple"></div></div>
<div class="abs thumb" style="left:396px"><div class="thumb-team" role="img" aria-label="Photo of a business team in suits"></div></div>
<div class="abs thumb" style="left:707px"><div class="thumb-globe" role="img" aria-label="Photo of a globe with a computer mouse"></div></div>

<div class="abs col-text" style="left:143px;top:717px">
  <p>kjnjkdfng dfgndfg dfgndfkgfndfgmk dnfgkdfngkdfg dfgkdfkgnkdfjkgnkn dkfgndfk dfklg dfkg kdf gdfg dfgfnf dfgndfkl dklg jdfng gjdfg dfjkdf ndf dfnmg dfgdfdmfg dfdfg dfgdf dfmd dfndfkg dfgmdfm</p>
  <p>dfgkdfgkdfkgmkdfgmk dfgmdfgfdfk dfgndfkgkdfmgkldmfgmkldfmmfdfk dkfmgkdfmgklmdfgmkldfg dfklgdfk dfkgmdlfmgdfkldf dkfg kldfgd fkdfg dflg,l;dfd</p>
</div>
<ul class="abs bullets" style="left:398px;top:722px;width:230px">
  <li>The jkxvjknjkdvx xjcvxcjvvxcjvjvxcn kv xcvxcvm,xv xc</li>
  <li>The jkxvjknjkdvx xjcvxcjvvxcjvjvxcn kv xcvxcvm,xv xc</li>
  <li>The jkxvjknjkdvx xjcvxcjvvxcjvjvxcn kv xcvxcvm,xv xc</li>
</ul>
<ul class="abs bullets" style="left:711px;top:720px;width:230px;word-break:break-all">
  <li>kdefnsdkfnsdnfksdsdfnsdsdjkfjkn sdkfkdsmkdskd</li>
  <li>sdjfnsjdnfdnsfsdfsdfdfdsfdnsfnsdjk</li>
  <li>sdjfnsd,fnksdfkdfksdkfkkdfs sndfns sdmfkldsm sdkfksdmk skldf sjkd sd sdkfmksdfm skdf skdf sdjkf sdjkfnsk skdfmklsdfksmdkfsdmfsdkfmkdm</li>
</ul>

<div class="abs footer-band"></div>
<h3 class="abs foot-title" style="left:144px">Social Network</h3>
<h3 class="abs foot-title" style="left:336px">About Us</h3>
<h3 class="abs foot-title" style="left:465px">Info</h3>
<h3 class="abs foot-title" style="left:580px">Discussion</h3>

<div class="abs social-row" style="left:148px;top:1031px"><span class="social-icon" style="background:var(--orange);border-radius:3px"></span><div>Become a Member !<br>Ajkng dfgndfgdfjk fgndfklgn</div></div>
<div class="abs social-row" style="left:148px;top:1073px"><span class="social-icon" style="background:#f5b82a;border-radius:50%;width:18px;height:18px"></span><div>Follow us on Chirper<br>Ajkng dfgndfgdfjk fgndfklgn</div></div>

<ul class="abs foot-links" style="left:340px;top:1025px"><li>Our Services</li><li>Our Services</li><li>Our Services</li></ul>
<ul class="abs foot-links" style="left:462px;top:1025px"><li>Clients Log In</li><li>Contact Us</li><li>Become Member</li><li>1800-04-6182</li></ul>
<ul class="abs foot-links" style="left:583px;top:1025px"><li>Our Community</li><li>Latest Updates</li><li>Latest Updates</li></ul>

<div class="abs newsletter">
  <h3>News Letter</h3>
  <div class="email-field">Your Email:<span class="email-go">»</span></div>
  <span class="subscribe">Suscripe Now</span>
</div>

<div class="abs bottom-bar"></div>
<div class="abs bottom-links">Home<span>|</span>About Us<span>|</span>Commerical<span>|</span>Residential<span>|</span>Contact Us</div>
<div class="abs rights">All Rights Reserved<span>|</span>Copyright &nbsp;&nbsp;2011</div>

</body>
</html>
```